Business Card Design Project

Velvet Harbor is a Boutique Clothing. On the business cards I would like to have this included
Website: www.velvetharbor-example.com
Email: shop@velvetharbor-example.com
Owner: Mai Torres & Bo Rinaldi

Industry/Entity Type

Business

Contact Information for Business Card

I wanted something simple and elegant. I have attach business logo.

```html
<!DOCTYPE html>
<html lang="en">
<head>
<meta charset="utf-8">
<title>Velvet Harbor – Business Card</title>
<link rel="stylesheet" href="https://fonts.googleapis.com/css2?family=Cormorant+Garamond:ital,wght@1,600&family=Questrial&display=swap">
<style>
  :root {
    --page-bg: #d8d4ce;
    --card-bg: #ffffff;
    --ink: #222222;
    --charcoal: #333333;
    --on-dark: #ffffff;
  }
  html, body {
    margin: 0;
    padding: 0;
    width: 1200px;
    height: 902px;
    overflow: hidden;
    background: var(--page-bg);
  }
  .card {
    position: absolute;
    left: 100px;
    top: 166px;
    width: 1000px;
    height: 569px;
    background: var(--card-bg);
    border-radius: 30px;
    overflow: hidden;
    box-shadow: 0 10px 30px rgba(0,0,0,0.18);
  }
  .card__band {
    position: absolute;
    inset: 0;
    width: 100%;
    height: 100%;
  }
  .brand {
    position: absolute;
    left: 84px;
    top: 190px;
    display: flex;
    align-items: center;
    gap: 14px;
    font-family: "Questrial", sans-serif;
    font-size: 34px;
    letter-spacing: 2px;
    color: var(--ink);
  }
  .brand__dot {
    width: 32px;
    height: 32px;
    border: 2px solid var(--ink);
    border-radius: 50%;
    box-sizing: border-box;
  }
  .owners {
    position: absolute;
    right: 51px;
    top: 58px;
    text-align: right;
    color: var(--ink);
  }
  .owners__names {
    font-family: "Cormorant Garamond", serif;
    font-style: italic;
    font-weight: 600;
    font-size: 40px;
    line-height: 1;
  }
  .owners__role {
    font-family: "Questrial", sans-serif;
    font-size: 21px;
    line-height: 1.2;
    margin-top: 2px;
  }
  .contacts {
    position: absolute;
    right: 48px;
    top: 448px;
    list-style: none;
    margin: 0;
    padding: 0;
    font-family: "Questrial", sans-serif;
    font-size: 23px;
    color: var(--on-dark);
  }
  .contacts__item {
    display: flex;
    align-items: center;
    justify-content: flex-end;
    gap: 10px;
    height: 40px;
  }
  .contacts__icon {
    width: 30px;
    height: 30px;
    flex: none;
  }
</style>
</head>
<body>
  <section class="card" aria-label="Velvet Harbor business card">
    <svg class="card__band" viewBox="0 0 1000 569" preserveAspectRatio="none" aria-hidden="true">
      <path fill="var(--charcoal)" d="M0 470 C250 520 450 420 620 350 C780 285 900 270 1000 280 L1000 569 L0 569 Z"/>
    </svg>

    <div class="brand">
      <span class="brand__dot"></span>
      <span class="brand__name">Velvet Harbor</span>
    </div>

    <div class="owners">
      <div class="owners__names">Mai Torres &amp; Bo Rinaldi</div>
      <div class="owners__role">Owner</div>
    </div>

    <ul class="contacts">
      <li class="contacts__item">
        <span>shop@velvetharbor-example.com</span>
        <svg class="contacts__icon" viewBox="0 0 30 30" aria-hidden="true">
          <circle cx="15" cy="15" r="13" fill="none" stroke="var(--on-dark)" stroke-width="2"/>
          <circle cx="15" cy="15" r="10" fill="var(--on-dark)"/>
          <rect x="9.5" y="11" width="11" height="8" fill="var(--charcoal)"/>
          <path d="M9.5 11 L15 15.5 L20.5 11" fill="none" stroke="var(--on-dark)" stroke-width="1.2"/>
        </svg>
      </li>
      <li class="contacts__item">
        <span>www.velvetharbor-example.com</span>
        <svg class="contacts__icon" viewBox="0 0 30 30" aria-hidden="true">
          <circle cx="15" cy="15" r="13" fill="none" stroke="var(--on-dark)" stroke-width="2"/>
          <circle cx="15" cy="15" r="10" fill="var(--on-dark)"/>
          <g fill="none" stroke="var(--charcoal)" stroke-width="1.1">
            <circle cx="15" cy="15" r="6"/>
            <ellipse cx="15" cy="15" rx="2.6" ry="6"/>
            <line x1="9" y1="15" x2="21" y2="15"/>
          </g>
        </svg>
      </li>
    </ul>
  </section>
</body>
</html>
```